Criação de Papelaria (6 itens) para Vértice & Aurora
" Funciona como dedetizadora como foco principal, possuindo a divisão dedetizadora ( controladora de pragas urbanas), a divisão hospitalar ( Comercio de equipamentos médico hospitalar), a divisão Higienização ( comércio de produtos de higiene e limpeza). O foco principal é a dedetizadora. "

```html
<!DOCTYPE html>
<html lang="pt-BR">
<head>
<meta charset="UTF-8">
<title>Vértice & Aurora – Papel timbrado</title>
<link href="https://fonts.googleapis.com/css2?family=Montserrat:wght@400;600;700;800&family=Open+Sans:wght@400;600&display=swap" rel="stylesheet">
<style>
  :root {
    --backdrop: #e6e7e8;
    --paper: #ffffff;
    --ink: #2a2a2a;
    --ink-soft: #6b6b6b;
    --text: #8a8a8a;
    --brand-red: #b5161d;
    --brand-dark: #1d1d1d;
    --wash: rgba(181, 22, 29, 0.06);
  }
  * { margin: 0; padding: 0; box-sizing: border-box; }
  html, body { width: 1200px; height: 1200px; overflow: hidden; }
  body {
    background: var(--backdrop);
    font-family: "Open Sans", Arial, sans-serif;
    position: relative;
  }
  .letterhead {
    position: absolute;
    left: 204px; top: 30px;
    width: 792px; height: 1140px;
    background: var(--paper);
    box-shadow: 0 10px 30px rgba(0,0,0,0.12);
    overflow: hidden;
  }
  .brand {
    position: absolute; right: 60px; top: 58px;
    display: flex; align-items: center; gap: 14px;
  }
  .brand-dot {
    width: 46px; height: 46px; border-radius: 50%;
    background: var(--brand-red);
  }
  .brand-text { text-align: left; }
  .brand-name {
    font-family: "Montserrat", Arial, sans-serif;
    font-weight: 800; font-size: 30px; color: var(--ink);
    letter-spacing: 0.5px; line-height: 1;
  }
  .brand-tagline {
    font-family: "Montserrat", Arial, sans-serif;
    font-weight: 800; font-size: 10px; color: var(--ink);
    letter-spacing: 4px; text-transform: uppercase; margin-top: 6px;
  }
  .watermark {
    position: absolute; left: 160px; top: 360px;
    width: 470px; height: 470px; border-radius: 50%;
    background: var(--wash);
  }
  .recipient {
    position: absolute; left: 70px; top: 66px;
    font-family: "Montserrat", Arial, sans-serif;
    font-weight: 700; font-size: 15px; line-height: 1.45; color: var(--ink);
  }
  .reference {
    position: absolute; right: 70px; top: 230px;
    font-size: 11px; line-height: 1.7; color: var(--ink-soft); text-align: right;
  }
  .letter-body {
    position: absolute; left: 70px; top: 290px; width: 650px;
    font-size: 12px; line-height: 1.9; color: var(--text);
  }
  .letter-body p { margin-bottom: 16px; text-align: justify; }
  .signature {
    position: absolute; left: 70px; top: 690px;
  }
  .signature-mark {
    width: 150px; height: 60px;
    background: linear-gradient(90deg, rgba(40,40,40,0.18), rgba(40,40,40,0.05));
    border-radius: 4px;
  }
  .signature-role { font-size: 11px; color: var(--ink-soft); margin-top: 8px; }
  .contacts {
    position: absolute; left: 70px; top: 1010px;
    display: grid; grid-template-columns: 260px 260px; row-gap: 10px;
    font-size: 11px; color: var(--ink-soft);
  }
  .contact { display: flex; align-items: center; gap: 8px; white-space: nowrap; }
  .contact svg { width: 12px; height: 12px; fill: var(--brand-red); flex: none; }
  .footer-bands { position: absolute; left: 0; bottom: 0; width: 792px; height: 70px; }
</style>
</head>
<body>
  <main class="letterhead">
    <div class="watermark" aria-hidden="true"></div>

    <div class="recipient">
      To<br>
      Mr. Daniel Prado<br>
      Chief Executive Officer<br>
      Northwind Studio<br>
      Campinas, SP 13025-470
    </div>

    <div class="brand">
      <span class="brand-dot" aria-hidden="true"></span>
      <div class="brand-text">
        <div class="brand-name">Vértice &amp; Aurora</div>
        <div class="brand-tagline">controle de pragas</div>
      </div>
    </div>

    <div class="reference">
      Referência: 0217<br>
      10 de abril de 2024
    </div>

    <section class="letter-body">
      <p>Agradecemos o contato e a confiança em nossos serviços. Apresentamos a seguir a proposta técnica para o controle integrado de pragas urbanas em suas instalações, com visitas mensais, relatórios detalhados e produtos registrados nos órgãos competentes.</p>
      <p>Nossa equipe atua também nas divisões hospitalar e de higienização, oferecendo equipamentos médicos e produtos de limpeza com a mesma qualidade e atenção que aplicamos em cada serviço de dedetização.</p>
      <p>Permanecemos à disposição para esclarecer dúvidas e agendar uma visita técnica sem compromisso.</p>
      <p>Atenciosamente,</p>
    </section>

    <div class="signature">
      <div class="signature-mark" role="img" aria-label="Assinatura manuscrita"></div>
      <div class="signature-role">Diretor Comercial</div>
    </div>

    <div class="contacts">
      <div class="contact">
        <svg viewBox="0 0 24 24" aria-hidden="true"><path d="M12 2a7 7 0 0 0-7 7c0 5 7 13 7 13s7-8 7-13a7 7 0 0 0-7-7zm0 9.5A2.5 2.5 0 1 1 12 6.5a2.5 2.5 0 0 1 0 5z"/></svg>
        Rua das Acácias, 120 – Campinas
      </div>
      <div class="contact">
        <svg viewBox="0 0 24 24" aria-hidden="true"><path d="M6.6 10.8a15 15 0 0 0 6.6 6.6l2.2-2.2a1 1 0 0 1 1-.25 11 11 0 0 0 3.6.6 1 1 0 0 1 1 1V20a1 1 0 0 1-1 1A17 17 0 0 1 3 4a1 1 0 0 1 1-1h3.5a1 1 0 0 1 1 1 11 11 0 0 0 .6 3.6 1 1 0 0 1-.25 1z"/></svg>
        +55 19 3517-6204
      </div>
      <div class="contact">
        <svg viewBox="0 0 24 24" aria-hidden="true"><circle cx="12" cy="12" r="10"/></svg>
        www.verticeaurora.com.br
      </div>
      <div class="contact">
        <svg viewBox="0 0 24 24" aria-hidden="true"><path d="M2 5h20v14H2zm2 2v.5l8 5 8-5V7z"/></svg>
        contato@verticeaurora.com.br
      </div>
    </div>

    <svg class="footer-bands" viewBox="0 0 792 70" preserveAspectRatio="none" aria-hidden="true">
      <defs>
        <linearGradient id="redFade" x1="0" x2="1">
          <stop offset="0" stop-color="#b5161d"/>
          <stop offset="0.75" stop-color="#b5161d"/>
          <stop offset="1" stop-color="#b5161d" stop-opacity="0.6"/>
        </linearGradient>
      </defs>
      <polygon points="0,30 330,52 0,52" fill="#1d1d1d"/>
      <polygon points="0,52 792,52 792,70 0,70" fill="url(#redFade)"/>
      <polygon points="0,44 792,60 792,52 0,52" fill="#b5161d" opacity="0.55"/>
    </svg>
  </main>
</body>
</html>
```